Makeup Artist Requires Business Card design

Hi

I am looking for a business card design to market my makeup artist business. I operate under my own name Hazel Drummet and I would like to keep the design of the card very simplistic and chic - something that keeps both my name and profession (makeup artist) the focus of the card. I would like it to be a style that is eyecatching to the reader (i am open to anything unusual) but upmarket.

Target Market(s)

women, magazine/beauty/fashion editors, photographers.

Industry/Entity Type

Business

Requirements
Must have
• Must contain:

Phone number: 0417 382 915
Website: www.hazeldrummet.com.au
email: contact@hazeldrummet.com.au

(although you don't need to have prefaced these with the words phone number, website etc :))
Should not have
• I am not looking for anything overly colorful - my preference is to keep the card dark if possible.

```html
<!DOCTYPE html>
<html lang="en">
<head>
<meta charset="utf-8">
<title>Hazel Drummet – Makeup Artist Business Card</title>
<link href="https://fonts.googleapis.com/css2?family=Open+Sans:wght@300;400&display=swap" rel="stylesheet">
<style>
  :root {
    --page-bg: #ececec;
    --card-black: #050505;
    --band-purple: #7d4f9c;
    --band-purple-light: #9a6bb8;
    --phone-bar: #4f6d86;
    --web-bar: #8c5ca8;
    --email-bar: #43285e;
    --text-light: #f2eef6;
    --text-dark: #1a2330;
    --text-lilac: #c3a6dc;
  }
  html, body {
    margin: 0;
    padding: 0;
    width: 1000px;
    height: 1200px;
    overflow: hidden;
    background: var(--page-bg);
  }
  .canvas {
    position: relative;
    width: 1000px;
    height: 1200px;
    background: var(--page-bg);
  }
  .business-card {
    position: absolute;
    left: 50px;
    top: 350px;
    width: 900px;
    height: 500px;
    background: var(--card-black);
    border-radius: 13% / 32%;
    overflow: hidden;
    box-shadow: 0 18px 40px rgba(0,0,0,0.35);
    font-family: "Open Sans", sans-serif;
  }
  .eye-photo {
    position: absolute;
    left: 397px;
    top: 0;
    width: 503px;
    height: 260px;
    background:
      radial-gradient(ellipse at 70% 45%, #d9d9dc 0%, #8f8f95 30%, rgba(40,40,44,0.6) 60%, rgba(5,5,5,0) 80%),
      linear-gradient(90deg, rgba(5,5,5,1) 0%, rgba(5,5,5,0) 35%);
  }
  .splatter-texture {
    position: absolute;
    left: 0;
    top: 140px;
    width: 640px;
    height: 360px;
    background: radial-gradient(ellipse at 35% 70%, rgba(70,40,90,0.75) 0%, rgba(40,22,55,0.5) 40%, rgba(5,5,5,0) 75%);
  }
  .name-band {
    position: absolute;
    left: 0;
    top: 215px;
    width: 900px;
    height: 67px;
    background: linear-gradient(90deg, var(--band-purple) 0%, var(--band-purple-light) 40%, rgba(125,79,156,0.35) 58%, rgba(5,5,5,0) 62%);
  }
  .name {
    position: absolute;
    left: 45px;
    top: 220px;
    margin: 0;
    font-weight: 400;
    font-size: 52px;
    line-height: 58px;
    letter-spacing: 0.5px;
    color: var(--text-light);
    text-transform: uppercase;
  }
  .profession {
    position: absolute;
    left: 542px;
    top: 232px;
    margin: 0;
    font-weight: 300;
    font-size: 42px;
    line-height: 46px;
    font-variant: small-caps;
    color: var(--text-light);
  }
  .contact-row {
    position: absolute;
    height: 46px;
    display: flex;
    align-items: center;
    justify-content: flex-end;
    padding-right: 14px;
    box-sizing: border-box;
    font-weight: 300;
    line-height: 46px;
  }
  .contact-icon {
    position: absolute;
    width: 38px;
    height: 38px;
    top: 4px;
  }
  .contact-phone { left: 520px; top: 328px; width: 368px; background: var(--phone-bar); color: var(--text-dark); font-size: 42px; }
  .contact-web { left: 318px; top: 377px; width: 570px; background: var(--web-bar); color: var(--text-dark); font-size: 40px; }
  .contact-email { left: 230px; top: 422px; width: 622px; background: var(--email-bar); color: var(--text-lilac); font-size: 38px; }
  .icon-phone { left: 476px; top: 332px; }
  .icon-web { left: 274px; top: 381px; }
  .icon-email { left: 186px; top: 426px; }
</style>
</head>
<body>
<main class="canvas">
  <section class="business-card">
    <div class="splatter-texture" role="img" aria-label="Dark purple ink splatter texture"></div>
    <div class="eye-photo" role="img" aria-label="Black and white close-up photograph of an eye with purple eyeshadow"></div>

    <div class="name-band"></div>
    <h1 class="name">Hazel Drummet</h1>
    <p class="profession">Makeup Artist</p>

    <svg class="contact-icon icon-phone" viewBox="0 0 38 38" aria-hidden="true">
      <circle cx="19" cy="19" r="16" fill="none" stroke="#e8e8ee" stroke-width="3"/>
      <path d="M13 11c-2 2-2 5 1 9s7 7 10 7c2 0 3-1 3-2l-3-3-2 1c-2-1-4-3-5-5l1-2-3-3z" fill="#e8e8ee"/>
    </svg>
    <div class="contact-row contact-phone">0417 382 915</div>

    <svg class="contact-icon icon-web" viewBox="0 0 38 38" aria-hidden="true">
      <g fill="none" stroke="#e2d6ec" stroke-width="2.5">
        <circle cx="19" cy="19" r="15"/>
        <ellipse cx="19" cy="19" rx="6" ry="15"/>
        <line x1="4" y1="19" x2="34" y2="19"/>
        <line x1="7" y1="11" x2="31" y2="11"/>
        <line x1="7" y1="27" x2="31" y2="27"/>
      </g>
    </svg>
    <div class="contact-row contact-web">www.hazeldrummet.com.au</div>

    <svg class="contact-icon icon-email" viewBox="0 0 38 38" aria-hidden="true">
      <g fill="none" stroke="#cdb8e0" stroke-width="2.5">
        <rect x="4" y="8" width="30" height="24"/>
        <path d="M4 20l15-10 15 10"/>
        <path d="M4 32l12-9M34 32l-12-9"/>
      </g>
    </svg>
    <div class="contact-row contact-email">contact@hazeldrummet.com.au</div>
  </section>
</main>
</body>
</html>
```